Stationary design for new digital markerting company

I need a stationary design for a new digital marketing company called Mossy Otter.
We work with businesses to help them create and increase their online presence in order to increase awareness of their brand.
The design must keep with the colour schemes of our logo.
I would like a design that stands out but isn't over the top while also being professional and sophisticated.

Target Market(s)

other businesses

Industry/Entity Type

Business Consultant

Font styles to use
Sans Serif

Colors
abd036
ffffff
a54499

Requirements
Must have
• logo, plus the same colour scheme

```html
<!DOCTYPE html>
<html lang="en">
<head>
<meta charset="utf-8">
<title>Mossy Otter — Business Card</title>
<link rel="stylesheet" href="https://fonts.googleapis.com/css2?family=Montserrat:wght@600&family=Questrial&display=swap">
<style>
  :root {
    --green: #abd036;
    --purple: #a54499;
    --purple-deep: #a0217f;
    --white: #ffffff;
    --paper: #f6f6f6;
    --ink: #3a3a3a;
    --backdrop: #e4e4e6;
    --shade: #e9e9e9;
  }
  * { box-sizing: border-box; margin: 0; padding: 0; }
  html, body { width: 1200px; height: 788px; overflow: hidden; }
  body {
    background: var(--backdrop);
    font-family: "Questrial", "Century Gothic", sans-serif;
    display: flex;
    align-items: center;
    justify-content: center;
    gap: 40px;
  }
  .card {
    position: relative;
    width: 520px;
    height: 300px;
    overflow: hidden;
    box-shadow: 0 10px 28px rgba(0,0,0,.16);
  }
  .card--front { background: var(--purple-deep); }
  .card--back { background: var(--paper); }

  .brand {
    position: absolute;
    display: flex;
    align-items: center;
    gap: 12px;
  }
  .brand__name {
    font-family: "Montserrat", sans-serif;
    font-weight: 600;
    font-size: 34px;
    letter-spacing: 1px;
    text-transform: uppercase;
    line-height: 1;
  }
  .brand__mark {
    width: 58px; height: 58px;
    border-radius: 50%;
    background: var(--green);
    flex: none;
  }
  .brand__tagline {
    position: absolute;
    font-size: 12px;
    letter-spacing: 2.6px;
    white-space: nowrap;
  }

  .card--front .brand { left: 100px; top: 112px; }
  .card--front .brand__name { color: var(--white); }
  .card--front .brand__tagline { left: 100px; top: 160px; color: var(--white); }

  .card--back .brand { left: 34px; top: 40px; }
  .card--back .brand__name { color: var(--purple); font-size: 26px; }
  .card--back .brand__mark { width: 46px; height: 46px; }
  .card--back .brand__tagline { left: 34px; top: 80px; color: var(--purple); font-size: 10px; letter-spacing: 2px; }

  .swoosh { position: absolute; left: 0; top: 0; width: 520px; height: 300px; }

  .contact {
    position: absolute;
    left: 262px;
    top: 118px;
    color: var(--ink);
  }
  .contact__name {
    font-family: "Montserrat", sans-serif;
    font-weight: 600;
    font-size: 17px;
    color: var(--purple);
    text-transform: uppercase;
    letter-spacing: .5px;
  }
  .contact__role { font-size: 14px; margin: 2px 0 10px; }
  .contact__list { list-style: none; font-size: 14px; line-height: 1.45; }
  .contact__item { display: flex; align-items: center; gap: 8px; }
  .contact__icon { width: 14px; height: 14px; flex: none; }
  .contact__address { font-size: 14px; line-height: 1.4; margin-top: 8px; }
</style>
</head>
<body>

  <section class="card card--front" aria-label="Business card front">
    <div class="brand">
      <span class="brand__name">Mossy Otter</span>
      <span class="brand__mark" aria-hidden="true"></span>
    </div>
    <p class="brand__tagline">Smart Growth for Bright Brands</p>
  </section>

  <section class="card card--back" aria-label="Business card back">
    <svg class="swoosh" viewBox="0 0 520 300" aria-hidden="true">
      <path d="M0 212 C120 220 210 250 300 300 L0 300 Z" fill="var(--shade)"/>
      <path d="M0 204 C130 210 230 246 320 300 L300 300 C210 252 120 222 0 216 Z" fill="var(--green)"/>
    </svg>

    <div class="brand">
      <span class="brand__name">Mossy Otter</span>
      <span class="brand__mark" aria-hidden="true"></span>
    </div>
    <p class="brand__tagline">Smart Growth for Bright Brands</p>

    <div class="contact">
      <h2 class="contact__name">Jamie Ellery</h2>
      <p class="contact__role">Managing Director</p>
      <ul class="contact__list">
        <li class="contact__item">
          <svg class="contact__icon" viewBox="0 0 14 14" aria-hidden="true"><rect width="14" height="14" rx="2" fill="var(--green)"/><path d="M4 3h2l1 2.5-1.2.8a6 6 0 0 0 2 2L8.5 7 11 8v2a1 1 0 0 1-1 1A7 7 0 0 1 3 4a1 1 0 0 1 1-1z" fill="#fff"/></svg>
          1300 555 018
        </li>
        <li class="contact__item">
          <svg class="contact__icon" viewBox="0 0 14 14" aria-hidden="true"><rect width="14" height="14" rx="2" fill="var(--green)"/><rect x="3" y="4" width="8" height="6" fill="none" stroke="#fff" stroke-width="1"/><path d="M3 4l4 3 4-3" fill="none" stroke="#fff" stroke-width="1"/></svg>
          info@mossyotter.com
        </li>
        <li class="contact__item">
          <svg class="contact__icon" viewBox="0 0 14 14" aria-hidden="true"><rect width="14" height="14" rx="2" fill="var(--green)"/><circle cx="7" cy="7" r="4" fill="none" stroke="#fff" stroke-width="1"/><path d="M3 7h8M7 3c-2 2.5-2 5.5 0 8M7 3c2 2.5 2 5.5 0 8" fill="none" stroke="#fff" stroke-width=".8"/></svg>
          www.mossyotter.com
        </li>
      </ul>
      <p class="contact__address">Level 12, Harbour House<br>18 Quay Lane, Sydney</p>
    </div>
  </section>

</body>
</html>
```